Bramblecrest Apparel and Nutrition is looking for a Clothing/Supplement Online Store Website!

Must be convenient, and user friendly, with vibrant colors that catch the eye!

Target Market(s)

Athletes, and Fashion Customers

Industry/Entity Type

Fitness

Coding

Coded - Design and coding required

Number of Pages Required

3 page

Font styles to use
Decorative

Colors

Designer to choose colors to be used in the design.

Requirements
Must have
• Somewhere to feature products, features to promote discounts and make announcements.
Nice to have
• My logos on each page

```html
<!DOCTYPE html>
<html lang="en">
<head>
<meta charset="utf-8">
<title>Bramblecrest Apparel and Nutrition</title>
<link rel="stylesheet" href="https://fonts.googleapis.com/css2?family=Catamaran:wght@400;500;600;700;800&family=Lato:wght@400;700&display=swap">
<style>
:root{
  --ink:#1b1b1b;
  --text:#3a3a3a;
  --muted:#6d6d6d;
  --paper:#ffffff;
  --mist:#ececec;
  --night:#141414;
  --strip:#2c2c2c;
  --accent:#f5c518;
  --pink:#e6246e;
  --teal:#39b2c4;
  --rule:#d7d7d7;
}
*{margin:0;padding:0;box-sizing:border-box}
html,body{width:1200px;height:3582px;overflow:hidden}
body{position:relative;background:var(--paper);font-family:"Lato",sans-serif;color:var(--text)}
.abs{position:absolute}

/* header */
.search{left:171px;top:24px;width:253px;height:35px;border:1px solid #cfcfcf;border-radius:18px;font-size:11px;font-style:italic;color:#888;padding:9px 12px}
.search svg{position:absolute;right:12px;top:10px}
.brand{font-family:"Catamaran",sans-serif;font-weight:800;color:var(--ink);letter-spacing:1px}
.brand-top{left:450px;top:50px;width:300px;text-align:center;font-size:30px}
.brand-top .dot{display:inline-block;width:12px;height:12px;border-radius:50%;background:#9a9a9a;margin-right:8px;vertical-align:4px}
.cart{right:170px;top:34px;display:flex;align-items:center;gap:6px;font-family:"Catamaran",sans-serif;font-weight:700;font-size:14px;color:var(--ink)}
.cart .price{color:#aaa;font-weight:500;margin-right:6px}
.cart .ico{width:26px;height:26px;border-radius:50%;background:var(--ink);display:flex;align-items:center;justify-content:center}
.nav{top:100px;font-family:"Catamaran",sans-serif;font-weight:700;font-size:14px;color:var(--ink);display:flex;gap:40px}
.nav.left{left:172px}.nav.right{right:173px}
.nav .on{position:relative}
.nav .on::after{content:"";position:absolute;left:2px;right:0;top:35px;height:3px;background:var(--ink)}

/* hero */
.hero-photo{left:0;top:143px;width:1200px;height:728px;background:linear-gradient(100deg,#5a5953 0%,#6e6a5f 30%,#8b8779 55%,#7a776c 100%)}
.hero-cut{left:0;top:740px}
.offer{left:593px;top:337px;width:445px;height:268px;border:4px solid #fff;color:#fff;text-align:center}
.offer .t1{position:absolute;left:0;right:0;top:50px;font-family:"Catamaran",sans-serif;font-weight:800;font-size:48px;line-height:1}
.offer .pct{position:absolute;left:45px;top:100px;font-family:"Catamaran",sans-serif;font-weight:800;font-size:112px;line-height:1;letter-spacing:-3px}
.offer .sale{position:absolute;left:268px;top:118px;font-family:"Catamaran",sans-serif;font-weight:800;font-size:58px;line-height:1}
.offer .today{position:absolute;left:272px;top:180px;font-family:"Catamaran",sans-serif;font-weight:700;font-size:17px;letter-spacing:2px}
.dots{left:577px;top:795px;display:flex;gap:4px}
.dots i{width:12px;height:12px;border-radius:50%;background:#b8b8b8}
.dots i.on{background:#fff}

/* about */
.about-bg{left:0;top:870px;width:1200px;height:430px;background:var(--mist)}
.about-art{left:215px;top:950px;width:355px;height:258px;border-radius:4px;background:linear-gradient(135deg,#3a383b,#8c2a45 55%,#4a4740)}
.about-title{left:595px;top:962px;font-family:"Catamaran",sans-serif;font-weight:800;font-size:31px;color:var(--ink)}
.about-text{left:596px;top:1018px;width:425px;font-size:11.2px;line-height:21px;color:#444}
.btn-dark{left:596px;top:1163px;width:118px;height:45px;background:var(--night);color:#fff;font-family:"Catamaran",sans-serif;font-weight:700;font-size:13px;display:flex;align-items:center;justify-content:center}

/* features */
.feat-bg{left:0;top:1299px;width:1200px;height:969px;background:radial-gradient(ellipse at 50% 40%,#262626,#0d0d0d 75%)}
.sec-title{left:0;width:1200px;text-align:center;font-family:"Catamaran",sans-serif;font-weight:800;font-size:32px}
.sec-sub{left:320px;width:560px;text-align:center;font-size:11.2px;line-height:21px}
.card{width:199px;height:313px;background:#fff;clip-path:polygon(0 14px,100% 0,100% 301px,0 100%);text-align:center}
.card::after{content:"";position:absolute;right:0;top:287px;width:70px;height:14px;background:#3a3a3a;clip-path:polygon(100% 0,100% 100%,0 100%)}
.card .pic{position:absolute;left:50px;top:20px;width:99px;height:140px;border-radius:6px}
.card .price{position:absolute;left:0;right:0;top:174px;font-family:"Catamaran",sans-serif;font-weight:700;font-size:17px;color:var(--ink)}
.card .desc{position:absolute;left:20px;right:20px;top:203px;font-size:11.5px;line-height:19px;color:#444}
.card .buy{position:absolute;left:58px;top:253px;width:83px;height:28px;border:1px solid #888;font-family:"Catamaran",sans-serif;font-weight:600;font-size:11px;color:#555;line-height:26px}
.card .buy.solid{background:var(--night);border-color:var(--night);color:#fff}
.badge{left:398px;top:1528px;width:40px;height:40px;border-radius:50%;background:var(--pink);color:#fff;font-family:"Catamaran",sans-serif;font-weight:700;font-size:11px;line-height:40px;text-align:center}

/* discounts */
.tile{overflow:hidden}
.deal{left:172px;top:2450px;width:417px;height:426px;background:linear-gradient(120deg,#1d1d1d,#3a3630 60%,#2a2723)}
.deal-brand{left:360px;top:2540px;width:190px;text-align:center;font-size:24px;color:#fff}
.deal .t{position:absolute;left:170px;width:240px;text-align:center;color:#fff;font-family:"Catamaran",sans-serif;font-weight:800;line-height:1}
.deal .t.yellow{color:var(--accent)}
.upto{left:608px;top:2450px;width:418px;height:204px;background:linear-gradient(90deg,#2fa7ba,#43bccc)}
.upto-photo{left:780px;top:2450px;width:230px;height:204px;background:linear-gradient(160deg,#e7c9b7,#d98fa0 50%,#4fbfc8)}
.upto .l{position:absolute;left:36px;color:#fff;font-family:"Catamaran",sans-serif;font-weight:800;line-height:1}
.code{position:absolute;left:37px;top:122px;width:114px;height:36px;border:2px dashed var(--accent);color:var(--accent);font-family:"Catamaran",sans-serif;font-weight:700;font-size:18px;text-align:center;line-height:33px}
.coll{left:608px;top:2672px;width:418px;height:204px;background:linear-gradient(90deg,#2e2628,#5a2a36 35%,#2b2223 70%,#1f1b1d)}
.yellow{color:var(--accent)}

/* service strip */
.strip{left:0;top:3013px;width:1200px;height:190px;background:var(--strip)}
.strip-cut{left:0;top:3125px}
.serv{top:3072px;display:flex;align-items:center;gap:10px;color:#fff}
.serv b{display:block;font-family:"Catamaran",sans-serif;font-weight:700;font-size:16px;line-height:18px}
.serv span{font-size:11px;color:#ddd}

/* footer */
.brand-foot{left:176px;top:3300px;font-size:27px}
.brand-foot .dot{display:inline-block;width:12px;height:12px;border-radius:50%;background:#9a9a9a;margin-right:8px;vertical-align:3px}
.phone-ico{left:171px;top:3404px;width:36px;height:36px;border-radius:50%;border:2px solid var(--ink);display:flex;align-items:center;justify-content:center}
.contact{left:214px;top:3398px;font-family:"Catamaran",sans-serif;color:var(--ink)}
.contact .a{font-size:16px;font-weight:600;line-height:18px}
.contact .b{font-size:21px;font-weight:700;line-height:26px}
.col{top:3256px}
.col h4{font-family:"Catamaran",sans-serif;font-weight:500;font-size:15px;color:var(--ink)}
.col h4::after{content:"";display:block;width:20px;height:2px;background:var(--ink);margin-top:12px;margin-bottom:11px}
.col li{list-style:none;font-size:10.5px;line-height:19px;color:#444}
.rule{left:172px;top:3505px;width:878px;height:1px;background:var(--rule)}
.social{left:172px;top:3538px;display:flex;gap:33px}
.social i{width:14px;height:14px;background:var(--ink);border-radius:3px}
.copy{left:643px;top:3540px;font-size:11px;color:#444}
</style>
</head>
<body>

<!-- header -->
<div class="abs search">Enter Keyword..
  <svg width="12" height="12" viewBox="0 0 12 12"><circle cx="5" cy="5" r="3.6" fill="none" stroke="#222" stroke-width="1.6"/><line x1="7.6" y1="7.6" x2="11" y2="11" stroke="#222" stroke-width="1.8"/></svg>
</div>
<div class="abs brand brand-top"><span class="dot"></span>BRAMBLECREST</div>
<div class="abs cart">Shopping Cart <span class="price">$0.00</span>
  <span class="ico"><svg width="12" height="12" viewBox="0 0 12 12"><path d="M1 2h2l1.5 6h5.5l1-4H4" fill="none" stroke="#fff" stroke-width="1.4"/><circle cx="5" cy="10.3" r="1" fill="#fff"/><circle cx="9" cy="10.3" r="1" fill="#fff"/></svg></span>
  <span class="ico"><svg width="12" height="12" viewBox="0 0 12 12"><circle cx="6" cy="4" r="2.6" fill="#fff"/><path d="M1.5 11.5c0-3 2-4.5 4.5-4.5s4.5 1.5 4.5 4.5z" fill="#fff"/></svg></span>
  <span class="ico"><svg width="12" height="12" viewBox="0 0 12 12"><path d="M6 10.5 1.6 6.2C.3 4.9.8 2.2 3.2 2.2c1.3 0 2.2 1 2.8 1.8.6-.8 1.5-1.8 2.8-1.8 2.4 0 2.9 2.7 1.6 4z" fill="#fff"/></svg></span>
</div>
<nav class="abs nav left"><span class="on">HOME</span><span>ABOUT</span><span>PRODUCTS</span></nav>
<nav class="abs nav right"><span>REVIEWS</span><span>BLOG</span><span>CONTACT US</span></nav>

<!-- hero -->
<div class="abs hero-photo" role="img" aria-label="Woman in a grey knit cardigan and sunglasses standing in a field of dry grass"></div>
<svg class="abs hero-cut" width="1200" height="131" viewBox="0 0 1200 131"><polygon points="0,8 600,131 1200,8 1200,131 0,131" fill="#ececec"/></svg>
<div class="abs offer">
  <div class="t1">NEW ARRIVALS</div>
  <div class="pct">25%</div>
  <div class="sale">SALE</div>
  <div class="today">OFFER TODAY</div>
</div>
<div class="abs dots"><i></i><i></i><i class="on"></i></div>

<!-- about -->
<div class="abs about-bg"></div>
<div class="abs about-art" role="img" aria-label="Model in a maroon hoodie photographed outdoors"></div>
<h2 class="abs about-title">ABOUT BRAMBLECREST</h2>
<p class="abs about-text">Lorem ipsum dolor sit amet, consectetur adipiscing elit, sed do eiusmod tempor incididunt ut labore et dolore magna aliqua. Ut enim ad minim veniam, quis nostr ud exercitation ullamco laboris nisi ut aliquip ex ea commodo consequat. Duis ute irure dolor in reprehenderit in voluptate velit esse cillum dolore eu fugiat nulla pariatur. Excepteur sint occaecat cupidatat non proident, sunt in culpa qui fficia deserunt mollit an</p>
<div class="abs btn-dark">READ MORE</div>

<!-- feature products -->
<div class="abs feat-bg" role="img" aria-label="Dark background with gym equipment"></div>
<h2 class="abs sec-title" style="top:1372px;color:#fff">FEATURE PRODUCTS</h2>
<p class="abs sec-sub" style="top:1425px;color:#eee">Lorem ipsum dolor sit amet, consectetur adipiscing elit, sed do eiusmod tempor incididunt ut labore et dolore magna aliqua. Ut enim ad minim veniam, quis nostrud exercitation ullamco labor</p>

<div class="abs card" style="left:171px;top:1502px"><div class="pic" role="img" aria-label="Red sleeveless dress" style="background:#d0202a"></div><div class="price">$250.00</div><div class="desc">Lorem ipsum dolor sit ame consec dum loetetudc</div><div class="buy solid">BUY NOW</div></div>
<div class="abs card" style="left:389px;top:1502px"><div class="pic" role="img" aria-label="White long sleeve top" style="background:#e6e6e6"></div><div class="price">$250.00</div><div class="desc">Lorem ipsum dolor sit ame consec dum loetetudc</div><div class="buy">BUY NOW</div></div>
<div class="abs card" style="left:608px;top:1502px"><div class="pic" role="img" aria-label="Coral leather handbag" style="background:#e8656b"></div><div class="price">$250.00</div><div class="desc">Lorem ipsum dolor sit ame consec dum loetetudc</div><div class="buy">BUY NOW</div></div>
<div class="abs card" style="left:826px;top:1502px"><div class="pic" role="img" aria-label="Yellow floral sundress" style="background:#d9c531"></div><div class="price">$250.00</div><div class="desc">Lorem ipsum dolor sit ame consec dum loetetudc</div><div class="buy">BUY NOW</div></div>

<div class="abs card" style="left:171px;top:1847px"><div class="pic" role="img" aria-label="Black supplement tub" style="background:#1e1e1e"></div><div class="price">$250.00</div><div class="desc">Lorem ipsum dolor sit ame consec dum loetetudc</div><div class="buy">BUY NOW</div></div>
<div class="abs card" style="left:389px;top:1847px"><div class="pic" role="img" aria-label="Red and navy plaid shirt" style="background:#5a2d3c"></div><div class="price">$250.00</div><div class="desc">Lorem ipsum dolor sit ame consec dum loetetudc</div><div class="buy">BUY NOW</div></div>
<div class="abs card" style="left:608px;top:1847px"><div class="pic" role="img" aria-label="Blue polka dot dress" style="background:#1f3c8e"></div><div class="price">$250.00</div><div class="desc">Lorem ipsum dolor sit ame consec dum loetetudc</div><div class="buy">BUY NOW</div></div>
<div class="abs card" style="left:826px;top:1847px"><div class="pic" role="img" aria-label="White supplement bottle" style="background:#e9e9e9"></div><div class="price">$250.00</div><div class="desc">Lorem ipsum dolor sit ame consec dum loetetudc</div><div class="buy">BUY NOW</div></div>
<div class="abs badge">SALE</div>

<!-- discounts -->
<h2 class="abs sec-title" style="top:2318px;color:var(--ink)">OUR DISCOUNTS</h2>
<p class="abs sec-sub" style="top:2373px;color:#444">Lorem ipsum dolor sit amet, consectetur adipiscing elit, sed do eiusmod tempor incididunt ut labore et dolore magna aliqua. Ut enim ad minim veniam, quis nostrud exercitation ullamco labor</p>

<div class="abs tile deal">
  <div class="abs" role="img" aria-label="Black shaker bottle with measuring tape and pills" style="left:0;top:0;width:200px;height:426px;background:linear-gradient(90deg,#141414,#2d2a26)"></div>
  <div class="t" style="top:214px;font-size:35px">DEAL OF</div>
  <div class="t" style="top:252px;font-size:56px">THE DAY</div>
  <div class="t yellow" style="top:322px;font-size:27px">GET 80% OFF</div>
</div>
<div class="abs brand deal-brand">BRAMBLECREST</div>

<div class="abs tile upto">
  <div class="l" style="top:72px;font-size:22px">UPTO 30%</div>
  <div class="l" style="top:95px;font-size:17px">ALL PRODUCTS</div>
  <div class="code">XGD342G</div>
</div>
<div class="abs upto-photo" role="img" aria-label="Excited woman in sunglasses holding colorful shopping bags"></div>

<div class="abs tile coll" role="img" aria-label="Woman in a maroon hoodie outdoors at dusk"></div>
<div class="abs" style="left:832px;top:2753px;color:#fff;font-family:'Catamaran',sans-serif;font-weight:800;line-height:1">
  <div style="font-size:22px">GET <span class="yellow">50%</span> OFF</div>
  <div style="font-size:18px;margin-top:4px">NEW COLLECTION</div>
</div>

<!-- service strip -->
<div class="abs strip"></div>
<svg class="abs strip-cut" width="1200" height="80" viewBox="0 0 1200 80"><polygon points="0,5 600,74 1200,5 1200,80 0,80" fill="#fff"/></svg>
<div class="abs serv" style="left:168px">
  <svg width="48" height="56" viewBox="0 0 48 56"><rect x="4" y="4" width="40" height="42" rx="7" fill="#fff"/><rect x="9" y="11" width="30" height="14" fill="#2c2c2c"/><circle cx="13" cy="36" r="3" fill="#2c2c2c"/><circle cx="35" cy="36" r="3" fill="#2c2c2c"/><rect x="8" y="46" width="8" height="8" fill="#fff"/><rect x="32" y="46" width="8" height="8" fill="#fff"/></svg>
  <div><b>Free Shipping</b><span>Ducimus qui blanditiis</span></div>
</div>
<div class="abs serv" style="left:388px">
  <svg width="38" height="48" viewBox="0 0 38 48"><path d="M9 20V12a10 10 0 0 1 20 0v8" fill="none" stroke="#fff" stroke-width="5"/><rect x="2" y="20" width="34" height="26" rx="3" fill="#fff"/></svg>
  <div><b>100% Secure</b><span>Ducimus qui blanditiis</span></div>
</div>
<div class="abs serv" style="left:600px">
  <svg width="62" height="40" viewBox="0 0 62 40"><rect x="9" y="3" width="44" height="29" rx="3" fill="none" stroke="#fff" stroke-width="3.5"/><rect x="1" y="33" width="60" height="5" rx="2" fill="#fff"/></svg>
  <div><b>Best Online</b><span>Ducimus qui blanditiis</span></div>
</div>
<div class="abs serv" style="left:824px">
  <svg width="60" height="54" viewBox="0 0 60 54"><circle cx="30" cy="12" r="10" fill="#fff"/><circle cx="11" cy="18" r="7" fill="#fff"/><circle cx="49" cy="18" r="7" fill="#fff"/><path d="M14 52c0-14 7-20 16-20s16 6 16 20z" fill="#fff"/><path d="M0 46c0-12 5-17 11-17 3 0 5 1 7 3-3 4-5 9-5 14z" fill="#fff"/><path d="M60 46c0-12-5-17-11-17-3 0-5 1-7 3 3 4 5 9 5 14z" fill="#fff"/></svg>
  <div><b>Customer Support</b><span>Ducimus qui blanditiis</span></div>
</div>

<!-- footer -->
<div class="abs brand brand-foot"><span class="dot"></span>BRAMBLECREST</div>
<div class="abs phone-ico"><svg width="18" height="18" viewBox="0 0 18 18"><path d="M4 1.5 6.5 5 5 7c1 2.3 3.5 4.8 6 6l2-1.5 3.5 2.5-1.5 3C8 16.5 1.5 10 1 3z" fill="#1b1b1b"/></svg></div>
<div class="abs contact"><div class="a">Contact Us:</div><div class="b">(555)-018-2740</div></div>

<div class="abs col" style="left:436px"><h4>Brands</h4><ul><li>Lorem ipsum</li><li>Dolor sit amet</li><li>Cnsectetur</li><li>Adipiscing eli</li><li>Sed do eiusmod</li><li>Dtempo</li><li>Sed do eiusmo</li></ul></div>
<div class="abs col" style="left:602px"><h4>Company</h4><ul><li>About Us</li><li>Product Reviews</li><li>Site Map</li><li>Discount Policies</li><li>Advanced Search</li><li>Affiliate</li><li>News</li></ul></div>
<div class="abs col" style="left:768px"><h4>My Account</h4><ul><li>My Account</li><li>Order History</li><li>Wish List</li><li>Newsletter</li><li>Our Products</li><li>Nutrition</li></ul></div>
<div class="abs col" style="left:925px"><h4>Customer Care</h4><ul><li>Order Info</li><li>Shipping / Tracking</li><li>Returns Info</li><li>Request Exchange</li><li>Guarantee</li></ul></div>

<div class="abs rule"></div>
<div class="abs social"><i></i><i></i><i></i><i></i></div>
<div class="abs copy">Copyright © 2019 All Rights reserved.Privacy Policy &nbsp;&nbsp; Terms &amp; Conditions</div>

</body>
</html>
```